Finally a Vodka produced for women ! (Label Design)

We are a small distillery based in Melbourne, Australia and we need a Vodka label design solution that will appeal to women aged 30-50 years and radiate luxury. Full Details are in a design brief attached. We thank you in advance.

Target Market(s)

Affluent females 30-50 years.

Industry/Entity Type

Spirits/Alcohol

Requirements
Must have
• Be clear this is a luxury Vodka.
Nice to have
• Elegance.

```html
<!DOCTYPE html>
<html lang="en">
<head>
<meta charset="utf-8">
<title>Velvet Wren Vodka – Label</title>
<link rel="stylesheet" href="https://fonts.googleapis.com/css2?family=Raleway:wght@200;300;500&family=Montserrat:wght@700&display=swap">
<style>
  :root {
    --backdrop: #7d527c;
    --outline: #2b1a2b;
    --ink: #111111;
    --ink-soft: #3a2a3a;
    --silver: #d3d3d8;
    --peach: #e7ab9c;
    --white: #ffffff;
  }
  html, body {
    margin: 0;
    padding: 0;
    width: 1200px;
    height: 1200px;
    overflow: hidden;
    background: var(--backdrop);
  }
  .label-canvas {
    position: relative;
    width: 1200px;
    height: 1200px;
    background: var(--backdrop);
    font-family: "Raleway", sans-serif;
  }
  .label-shape {
    position: absolute;
    inset: 0;
  }
  .brand-square {
    position: absolute;
    left: 565px;
    top: 330px;
    width: 70px;
    height: 70px;
    background: var(--ink);
  }
  .brand-name {
    position: absolute;
    left: 0;
    width: 1200px;
    text-align: center;
    color: var(--silver);
    font-weight: 300;
    line-height: 1;
    margin: 0;
  }
  .brand-name--line {
    font-size: 64px;
    letter-spacing: 10px;
    padding-left: 10px;
  }
  .brand-name--one { top: 480px; }
  .brand-name--two { top: 540px; }
  .brand-name--sub {
    top: 612px;
    font-size: 26px;
    letter-spacing: 12px;
    padding-left: 12px;
  }
  .rose-artwork {
    position: absolute;
    left: 392px;
    top: 668px;
    width: 420px;
    height: 340px;
    border-radius: 48% 52% 44% 46%;
    background: radial-gradient(ellipse at 58% 42%, rgba(214, 214, 220, 0.55), rgba(231, 171, 156, 0.55) 55%, rgba(231, 171, 156, 0) 100%);
  }
  .product-name {
    position: absolute;
    left: 0;
    width: 1200px;
    top: 852px;
    text-align: center;
    font-weight: 200;
    font-size: 82px;
    letter-spacing: 46px;
    padding-left: 46px;
    color: var(--ink);
    line-height: 1;
    margin: 0;
  }
  .strength {
    position: absolute;
    left: 418px;
    top: 960px;
    font-size: 21px;
    line-height: 1.05;
    letter-spacing: 2px;
    color: var(--ink-soft);
    font-weight: 300;
  }
  .strength strong { font-weight: 500; display: block; color: var(--ink); }
  .strength span { display: block; }
  .volume {
    position: absolute;
    left: 728px;
    top: 1020px;
    font-size: 21px;
    letter-spacing: 3px;
    color: var(--ink-soft);
    font-weight: 300;
  }
  .origin {
    position: absolute;
    left: 0;
    width: 1200px;
    text-align: center;
    font-family: "Montserrat", sans-serif;
    font-weight: 700;
    font-size: 20px;
    line-height: 1;
  }
  .origin--bottled { top: 1092px; color: var(--ink); }
  .origin--city { top: 1114px; color: var(--white); }
  .origin--country { top: 1135px; color: var(--white); }
</style>
</head>
<body>
  <main class="label-canvas">
    <svg class="label-shape" width="1200" height="1200" viewBox="0 0 1200 1200" aria-hidden="true">
      <polygon points="489,1112 711,1112 600,1180" fill="var(--peach)"/>
      <polygon points="600,40 968,956 600,1180 236,956" fill="none" stroke="var(--outline)" stroke-width="1.6"/>
    </svg>

    <div class="brand-square"></div>
    <p class="brand-name brand-name--line brand-name--one">VELVET</p>
    <p class="brand-name brand-name--line brand-name--two">WREN</p>
    <p class="brand-name brand-name--sub">DISTILLERY</p>

    <div class="rose-artwork" role="img" aria-label="Geometric line drawing of a peach rose with a silver outline of the Australian continent over it"></div>

    <h1 class="product-name">VODKA</h1>

    <div class="strength"><strong>40%</strong><span>ALC/</span><span>VOL</span></div>
    <div class="volume">700m</div>

    <div class="origin origin--bottled">Bottled In</div>
    <div class="origin origin--city">Melbourne</div>
    <div class="origin origin--country">Australia</div>
  </main>
</body>
</html>
```